Update current boring label!!

Help! We need to have our current label redesigned. Initially it was ok but now it needs more punch. We have 3 different products. Vinaigrettes, Balsamic Glazes, and flavored olive oils. I want the same label for all 3 but perhaps in different colors to set the 3 apart. I like clean lines and need something that will be easier to read. Colors I like are black, white, golds, greens and browns.

I like some of the olive oil labels that are out there as they are very clear and easy to read. Same holds true with some Champagne labels.

You all have been so terrific in the past I hope someone can generate a new and wonderful look.

I have attached the current label to use for size.

I look forward to seeing all your wonderful designs.
Updates

Designers,I went on framevault and asked to see all the olive oil labels and there were many labels that I liked a lot. The vintage look is amazing, so please check them out to get an overall feel for what we are looking for.Many thanks,Lorna Added Wednesday, August 9, 2017

Reason: I feel like the label still needs some work. Am looking for that design that without tasting our product SELLS IT!

Target Market(s)

Upscale food buyers. Our products are on the upper end of the spectrum and cost a bit more than others due to their high quality ingredients

Font styles to use
Serif
Decorative
Script

Colors

Designer to choose colors to be used in the design.

Requirements
Must have
• A label that stands out. I see all the wonderful labels that are out there and want something that looks like it's worth more money.
• I would like Marlow to be have more of a punch as well.
Nice to have
• I like the look of white labels with wonderful designs that are easy to read and really stand out. Right now our product is basically plain. The look of champagne labels and olive oil labels. You can get a feel for what I am looking for by looking on line at the different types of labels on bottles.
Should not have
• No pictures just print

```html
<!DOCTYPE html>
<html lang="en">
<head>
<meta charset="utf-8">
<title>Marlow Label Series</title>
<link href="https://fonts.googleapis.com/css2?family=Playfair+Display:wght@400;700;900&family=Oswald:wght@500;600&family=Roboto+Condensed:wght@700&display=swap" rel="stylesheet">
<style>
  :root {
    --canvas: #ffffff;
    --label-white: #f6f6f6;
    --label-edge: #e4e4e4;
    --ink: #1c1c1c;
    --ink-light: #ffffff;
    --band-red: #cf2a2a;
    --band-red-dark: #a81e1e;
    --frame-gold: #e7b21e;
    --frame-orange: #f2a11f;
    --star: #f08a12;
  }
  html, body {
    margin: 0;
    padding: 0;
    width: 1200px;
    height: 1200px;
    overflow: hidden;
    background: var(--canvas);
  }
  .label-row {
    width: 1200px;
    height: 1200px;
    display: flex;
    justify-content: space-evenly;
    align-items: center;
  }
  .label { width: 341px; height: 688px; display: block; }
  .brand { font-family: "Playfair Display", serif; font-weight: 900; }
  .tagline { font-family: "Playfair Display", serif; font-weight: 400; font-size: 8px; }
  .product-name { font-family: "Playfair Display", serif; font-weight: 900; }
  .band-text { font-family: "Oswald", sans-serif; font-weight: 600; font-size: 31px; fill: var(--ink-light); letter-spacing: -0.5px; }
  .stars { font-family: sans-serif; font-size: 9px; fill: var(--star); letter-spacing: 3px; }
  .volume { font-family: "Roboto Condensed", sans-serif; font-weight: 700; font-size: 9px; fill: var(--ink); }
  .label-oil .brand, .label-oil .tagline, .label-oil .product-name { fill: var(--ink-light); }
  .label-glaze .brand, .label-glaze .tagline, .label-glaze .product-name,
  .label-vinaigrette .brand, .label-vinaigrette .tagline, .label-vinaigrette .product-name { fill: var(--ink); }
</style>
</head>
<body>
<main class="label-row">

  <!-- Olive oil label -->
  <svg class="label label-oil" viewBox="0 0 310 625" role="img" aria-label="Marlow Basil Infused Olive Oil label">
    <defs>
      <linearGradient id="oil-panel" x1="0" y1="0" x2="0" y2="1">
        <stop offset="0" stop-color="#3f8a2b"/>
        <stop offset="1" stop-color="#7cb83e"/>
      </linearGradient>
      <linearGradient id="oil-paper" x1="0" y1="0" x2="1" y2="0">
        <stop offset="0" stop-color="#e2e2e2"/>
        <stop offset="0.1" stop-color="#f7f7f7"/>
        <stop offset="0.9" stop-color="#f7f7f7"/>
        <stop offset="1" stop-color="#e2e2e2"/>
      </linearGradient>
      <linearGradient id="oil-band" x1="0" y1="0" x2="0" y2="1">
        <stop offset="0" stop-color="#d83030"/>
        <stop offset="1" stop-color="#b82222"/>
      </linearGradient>
    </defs>
    <rect class="paper" x="0" y="0" width="310" height="625" fill="url(#oil-paper)"/>
    <path class="panel" d="M32 17 L262 17 L282 37 L282 375 L12 375 L12 37 Z" fill="url(#oil-panel)"/>
    <path class="panel-frame" d="M22 375 L22 43 L38 27 L256 27 L272 43 L272 375" fill="none" stroke="var(--frame-gold)" stroke-width="1.5"/>
    <text class="brand" x="148" y="99" font-size="48" text-anchor="middle" textLength="180" lengthAdjust="spacingAndGlyphs">MARLOW</text>
    <text class="tagline" x="148" y="114" text-anchor="middle" textLength="180" lengthAdjust="spacingAndGlyphs">WONDERFULLY | INDULGENT | DRESSING</text>
    <text class="product-name" x="148" y="186" font-size="50" text-anchor="middle" textLength="180" lengthAdjust="spacingAndGlyphs">BASIL</text>
    <text class="product-name" x="148" y="227" font-size="40" text-anchor="middle" textLength="180" lengthAdjust="spacingAndGlyphs">INFUSED</text>
    <text class="product-name" x="148" y="276" font-size="56" text-anchor="middle" textLength="180" lengthAdjust="spacingAndGlyphs">OLIVE</text>
    <text class="product-name" x="148" y="333" font-size="66" text-anchor="middle" textLength="180" lengthAdjust="spacingAndGlyphs">O I L</text>
    <rect class="band" x="12" y="375" width="270" height="52" fill="url(#oil-band)"/>
    <text class="band-text" x="147" y="412" text-anchor="middle" textLength="216" lengthAdjust="spacingAndGlyphs">PREMIUM PRODUCT</text>
    <path class="base-frame" d="M22 427 L22 580 L44 600 L250 600 L272 580 L272 427" fill="none" stroke="var(--frame-orange)" stroke-width="1.5"/>
    <text class="stars" x="148" y="527" text-anchor="middle">★★★★★</text>
    <text class="volume" x="148" y="564" text-anchor="middle">8.5 fl oz 250 ml</text>
    <text class="volume" x="148" y="575" text-anchor="middle">PRODUCT OF ITALY</text>
  </svg>

  <!-- Balsamic glaze label -->
  <svg class="label label-glaze" viewBox="0 0 310 625" role="img" aria-label="Marlow Mixed Berry Balsamic Glaze label">
    <defs>
      <linearGradient id="glaze-panel" x1="0" y1="0" x2="0" y2="1">
        <stop offset="0" stop-color="#8a8a88"/>
        <stop offset="0.5" stop-color="#e0e0dc"/>
        <stop offset="1" stop-color="#7a7a78"/>
      </linearGradient>
      <linearGradient id="glaze-paper" x1="0" y1="0" x2="1" y2="0">
        <stop offset="0" stop-color="#e2e2e2"/>
        <stop offset="0.1" stop-color="#f7f7f7"/>
        <stop offset="0.9" stop-color="#f7f7f7"/>
        <stop offset="1" stop-color="#e2e2e2"/>
      </linearGradient>
      <linearGradient id="glaze-band" x1="0" y1="0" x2="0" y2="1">
        <stop offset="0" stop-color="#d83030"/>
        <stop offset="1" stop-color="#b82222"/>
      </linearGradient>
    </defs>
    <rect class="paper" x="0" y="0" width="310" height="625" fill="url(#glaze-paper)"/>
    <path class="panel" d="M32 17 L262 17 L282 37 L282 375 L12 375 L12 37 Z" fill="url(#glaze-panel)"/>
    <path class="panel-frame" d="M22 375 L22 43 L38 27 L256 27 L272 43 L272 375" fill="none" stroke="var(--frame-gold)" stroke-width="1.5"/>
    <text class="brand" x="148" y="99" font-size="48" text-anchor="middle" textLength="180" lengthAdjust="spacingAndGlyphs">MARLOW</text>
    <text class="tagline" x="148" y="114" text-anchor="middle" textLength="180" lengthAdjust="spacingAndGlyphs">WONDERFULLY | INDULGENT | DRESSING</text>
    <text class="product-name" x="148" y="200" font-size="50" text-anchor="middle" textLength="180" lengthAdjust="spacingAndGlyphs">MIXED</text>
    <text class="product-name" x="148" y="244" font-size="50" text-anchor="middle" textLength="180" lengthAdjust="spacingAndGlyphs">BERRY</text>
    <text class="product-name" x="148" y="280" font-size="36" text-anchor="middle" textLength="180" lengthAdjust="spacingAndGlyphs">BALSAMIC</text>
    <text class="product-name" x="148" y="331" font-size="56" text-anchor="middle" textLength="180" lengthAdjust="spacingAndGlyphs">GLAZE</text>
    <rect class="band" x="12" y="375" width="270" height="52" fill="url(#glaze-band)"/>
    <text class="band-text" x="147" y="412" text-anchor="middle" textLength="216" lengthAdjust="spacingAndGlyphs">PREMIUM PRODUCT</text>
    <path class="base-frame" d="M22 427 L22 580 L44 600 L250 600 L272 580 L272 427" fill="none" stroke="var(--frame-orange)" stroke-width="1.5"/>
    <text class="stars" x="148" y="527" text-anchor="middle">★★★★★</text>
    <text class="volume" x="148" y="564" text-anchor="middle">8.5 fl oz 250 ml</text>
    <text class="volume" x="148" y="575" text-anchor="middle">PRODUCT OF ITALY</text>
  </svg>

  <!-- Vinaigrette label -->
  <svg class="label label-vinaigrette" viewBox="0 0 310 625" role="img" aria-label="Marlow Champagne Pear Vinaigrettes label">
    <defs>
      <linearGradient id="vin-panel" x1="0" y1="0" x2="0" y2="1">
        <stop offset="0" stop-color="#b9a566"/>
        <stop offset="0.55" stop-color="#e3d49f"/>
        <stop offset="1" stop-color="#c9b67a"/>
      </linearGradient>
      <linearGradient id="vin-paper" x1="0" y1="0" x2="1" y2="0">
        <stop offset="0" stop-color="#e2e2e2"/>
        <stop offset="0.1" stop-color="#f7f7f7"/>
        <stop offset="0.9" stop-color="#f7f7f7"/>
        <stop offset="1" stop-color="#e2e2e2"/>
      </linearGradient>
      <linearGradient id="vin-band" x1="0" y1="0" x2="0" y2="1">
        <stop offset="0" stop-color="#d83030"/>
        <stop offset="1" stop-color="#b82222"/>
      </linearGradient>
    </defs>
    <rect class="paper" x="0" y="0" width="310" height="625" fill="url(#vin-paper)"/>
    <path class="panel" d="M32 17 L262 17 L282 37 L282 375 L12 375 L12 37 Z" fill="url(#vin-panel)"/>
    <path class="panel-frame" d="M22 375 L22 43 L38 27 L256 27 L272 43 L272 375" fill="none" stroke="var(--frame-gold)" stroke-width="1.5"/>
    <text class="brand" x="148" y="99" font-size="48" text-anchor="middle" textLength="180" lengthAdjust="spacingAndGlyphs">MARLOW</text>
    <text class="tagline" x="148" y="114" text-anchor="middle" textLength="180" lengthAdjust="spacingAndGlyphs">WONDERFULLY | INDULGENT | DRESSING</text>
    <text class="product-name" x="148" y="194" font-size="27" text-anchor="middle" textLength="178" lengthAdjust="spacingAndGlyphs">CHAMPAGNE</text>
    <text class="product-name" x="148" y="252" font-size="64" text-anchor="middle" textLength="178" lengthAdjust="spacingAndGlyphs">PEAR</text>
    <text class="product-name" x="148" y="278" font-size="22" text-anchor="middle" textLength="176" lengthAdjust="spacingAndGlyphs">VINAIGRETTES</text>
    <rect class="band" x="12" y="375" width="270" height="52" fill="url(#vin-band)"/>
    <text class="band-text" x="147" y="412" text-anchor="middle" textLength="216" lengthAdjust="spacingAndGlyphs">PREMIUM PRODUCT</text>
    <path class="base-frame" d="M22 427 L22 580 L44 600 L250 600 L272 580 L272 427" fill="none" stroke="var(--frame-orange)" stroke-width="1.5"/>
    <text class="stars" x="148" y="527" text-anchor="middle">★★★★★</text>
    <text class="volume" x="148" y="564" text-anchor="middle">8.5 fl oz 250 ml</text>
    <text class="volume" x="148" y="575" text-anchor="middle">PRODUCT OF ITALY</text>
  </svg>

</main>
</body>
</html>
```